Therapy Dog Business need a brochure

I need a brochure designed for my Canine Assisted Therapy business in Victoria Australia. I have a logo already and info and photos to upload.
Best as white background and using the colours from the logo please
Updates

Hi Everyone,
I am sorry to have to revise the brief. I have added three new photos I was unable to add due to the size. I have had to wait for my photographer to change the size to add them today. I have been really inspired by all the work you have done so far. Thank you.
Could you please add the following on the brochure. (Under the individual dogs photo)
1. Juniper is the white dog. Please add the following under her picture. Juniper is one of the first Court Dogs in Australia. Working in Victoria, she has worked in the following Courts. The Ostrander Inquest Bench, The Dunmore Justice Hall in Collingwood, and the Brackwell Tribunal in Melbourne CBD. Her ability to use her intuition for clients is inspiring. Please contact us for potential use in Courts. Juniper has worked at the Harrowgate Safety College, and at STAVE at Har Saf. She is a stunning dog!
2. Barnaby is the golden dog. Barnaby is Junipers son, and had her instinct of intuition of who needs his help. Barnaby has an incredible soft approach as does his mother Juniper. He is incredibly safe with young children, and yet has a playful nature for adolescents and adults alike. He is soft and caring, and like his mother will go to those who need him most. Barnaby like his mother has worked at Harrowgate Safety, his time at HS included the Harrowgate Safety Council (HSC) Both he and his mother have very impressive CV'S!
3. Pepper the black dog. Pepper is my Therapy and Assistance dog "trainer" she is safe and stable with all the dogs and people I train for Therapy Dog Training and Assistance Dog Training. She has also been with me on my journey as a Counsellor and I have been able to work alongside her and Juniper for Counselling sessions.
She is soft, caring, and also intuitive. I am incredibly grateful for her help, as well as Juniper and Barnaby.
ALSO I am so sorry to add this but could you also add the following: Maybe in dot point?
Court Dog Availability
Therapy Dog Visits - Lawyers - Courts - Child Protection
Police Station / Ambulance Station / Fire Station - Visits
Private Therapy Dog Sessions
website and email confirmation coming soon. Thank you

3. Pepper the black dog.

Target Market(s)

First Responders

Requirements
Must have
• All the photos provided.
Should not have
• Generic photos

```html
<!DOCTYPE html>
<html lang="en">
<head>
<meta charset="utf-8">
<title>Canine Assisted Therapy – Brochure</title>
<link rel="stylesheet" href="https://fonts.googleapis.com/css2?family=Montserrat:wght@300;400;500;600;700&display=swap">
<style>
  :root {
    --backdrop: #e6e6e6;
    --sheet: #ffffff;
    --panel: #f4f1ec;
    --ink-dark: #2e1116;
    --ink-body: #2a2222;
    --ink-soft: #6b5a4a;
    --ink-brand: #4a3a30;
    --leaf: #a8332a;
    --photo-blue: #8fa3d6;
    --photo-cream: #e8dcc4;
    --photo-gold: #c9a36a;
    --photo-black: #2a2a2c;
    --box-line: #b8b2aa;
  }
  * { box-sizing: border-box; margin: 0; padding: 0; }
  html, body { width: 1200px; height: 1000px; overflow: hidden; }
  body { background: var(--backdrop); font-family: "Montserrat", sans-serif; position: relative; }

  .sheet { position: absolute; left: 40px; top: 103px; width: 1120px; height: 794px; background: var(--sheet); }
  .panel { position: absolute; top: 127px; height: 745px; background: var(--panel); }
  .panel--dogs { left: 62px; width: 328px; }
  .panel--invite { left: 432px; width: 336px; }
  .panel--cover { left: 810px; width: 327px; }

  .photo { position: absolute; border: 6px solid #fff; box-shadow: 2px 4px 8px rgba(0,0,0,.28); }
  .photo--juniper { left: 72px; top: 145px; width: 130px; height: 122px; transform: rotate(-3deg);
    background: linear-gradient(135deg, var(--photo-blue), var(--photo-cream) 55%, #d9c8a6); }
  .photo--barnaby { left: 243px; top: 306px; width: 132px; height: 124px; transform: rotate(2deg);
    background: linear-gradient(135deg, var(--photo-blue), var(--photo-gold) 55%, #b58a50); }
  .photo--pepper { left: 72px; top: 474px; width: 130px; height: 124px; transform: rotate(-2deg);
    background: linear-gradient(135deg, var(--photo-blue), var(--photo-black) 50%, #1c1c1e); }
  .photo--trio { left: 835px; top: 382px; width: 276px; height: 180px;
    background: linear-gradient(180deg, #a86a4e 0%, #b07a5c 32%, var(--photo-blue) 40%, #7f95cc 100%); }

  .dog-bio { position: absolute; font-size: 7.8px; line-height: 9.8px; color: var(--ink-body); }
  .dog-bio--juniper { left: 217px; top: 149px; width: 168px; }
  .dog-bio--barnaby { left: 82px; top: 305px; width: 152px; }
  .dog-bio--pepper { left: 216px; top: 473px; width: 168px; }

  .availability { position: absolute; left: 83px; top: 626px; width: 289px; height: 115px;
    background: #fff; border: 1px solid var(--box-line); padding: 12px 10px; }
  .availability h3 { font-size: 11px; font-weight: 600; color: var(--ink-dark); text-align: center; margin-bottom: 10px; }
  .availability ul { list-style: none; font-size: 9px; color: var(--ink-body); white-space: nowrap; }
  .availability li { margin-bottom: 9.5px; }
  .availability li::before { content: "·"; margin-right: 5px; }

  .leaf-mark { position: absolute; width: 46px; height: 46px; border-radius: 6px;
    background: var(--leaf); opacity: .85; }
  .leaf-mark--dogs { left: 204px; top: 772px; }
  .leaf-mark--cover { left: 950px; top: 770px; }

  .invite-title { position: absolute; left: 432px; top: 194px; width: 336px; text-align: center;
    font-size: 30px; font-weight: 700; line-height: 32px; color: var(--ink-dark); }
  .invite-copy { position: absolute; left: 432px; top: 275px; width: 336px; text-align: center;
    font-size: 16.5px; font-weight: 400; line-height: 30px; color: var(--ink-soft); white-space: nowrap; }

  .brand { position: absolute; display: flex; flex-direction: column; align-items: center; text-align: center; }
  .brand__dot { display: block; border-radius: 50%; border: 2px solid var(--ink-dark); }
  .brand__name { font-weight: 600; color: var(--ink-dark); letter-spacing: 1px; white-space: nowrap; }
  .brand--small { left: 556px; top: 652px; width: 88px; }
  .brand--small .brand__dot { width: 88px; height: 88px; }
  .brand--cover { left: 810px; top: 196px; width: 327px; }
  .brand--cover .brand__dot { width: 124px; height: 124px; }
  .brand--cover .brand__name { font-size: 15px; margin-top: 10px; }

  .contact { position: absolute; left: 432px; top: 754px; width: 336px; text-align: center; color: var(--ink-brand); }
  .contact__name { font-size: 13px; font-weight: 600; letter-spacing: 2.5px; margin-bottom: 4px; }
  .contact p { font-size: 11.5px; line-height: 17px; }
  .contact a { color: var(--ink-brand); }

  .cover-title { position: absolute; left: 810px; top: 606px; width: 327px; text-align: center;
    font-size: 46px; font-weight: 500; line-height: 45px; color: var(--ink-dark); }
</style>
</head>
<body>
  <div class="sheet"></div>

  <section class="panel panel--dogs"></section>
  <section class="panel panel--invite"></section>
  <section class="panel panel--cover"></section>

  <!-- Dogs panel -->
  <div class="photo photo--juniper" role="img" aria-label="Portrait of Juniper, a white Labrador, on a blue blanket"></div>
  <p class="dog-bio dog-bio--juniper">Juniper is one of the first Court Dogs in Australia. Working in Victoria, she has worked in the following Courts. The Ostrander Inquest Bench, The Dunmore Justice Hall in Collingwood, and the Brackwell Tribunal in Melbourne CBD. Her ability to use her intuition for clients is inspiring. Please contact us for potential use in Courts. Juniper has worked at the Harrowgate Safety College, and at STAVE at Har Saf. She is a stunning dog!</p>

  <p class="dog-bio dog-bio--barnaby">Barnaby is Junipers son, and had her instinct of intuition of who needs his help. Barnaby has an incredible soft approach as does his mother Juniper. He is incredibly safe with young children, and yet has a playful nature for adolescents and adults alike. He is soft and caring, and like his mother will go to those who need him most. Barnaby like his mother has worked at Harrowgate Safety, his time at HS included the Harrowgate Safety Council (HSC). Both he and his mother have very impressive CV'S!</p>
  <div class="photo photo--barnaby" role="img" aria-label="Portrait of Barnaby, a golden Labrador, on a blue blanket"></div>

  <div class="photo photo--pepper" role="img" aria-label="Portrait of Pepper, a black Labrador, on a blue blanket"></div>
  <p class="dog-bio dog-bio--pepper">Pepper is my Therapy and Assistance dog "trainer" she is safe and stable with all the dogs and people I train for Therapy Dog Training and Assistance Dog Training. She has also been with me on my journey as a Counsellor and I have been able to work alongside her and Juniper for Counselling sessions. She is soft, caring, and also intuitive. I am incredibly grateful for her help, as well as Juniper and Barnaby.</p>

  <div class="availability">
    <h3>Court Dog Availability</h3>
    <ul>
      <li>Therapy Dog Visits - Lawyers - Courts - Child Protection</li>
      <li>Police Station / Ambulance Station / Fire Station - Visits</li>
      <li>Private Therapy Dog Sessions</li>
    </ul>
  </div>
  <div class="leaf-mark leaf-mark--dogs" role="img" aria-label="Red maple leaf ornament"></div>

  <!-- Invitation panel -->
  <h2 class="invite-title">Join the Healing<br>Journey Today!</h2>
  <p class="invite-copy">Whether you are seeking<br>emotional support or mental<br>health improvement,<br>Canine Assisted Therapy<br>offers a unique and<br>compassionate approach<br>to healing.<br>Connect with us today<br>to learn more about how<br>a therapy dog can help<br>enhance your life<br>and well-being.</p>

  <div class="brand brand--small">
    <span class="brand__dot"></span>
  </div>
  <div class="contact">
    <p class="contact__name">GENTLE PAW THERAPY</p>
    <p>0491 570 156</p>
    <p><a href="#">www.gentlepawtherapy.com</a></p>
    <p><a href="#">hello@gentlepawtherapy.com</a></p>
  </div>

  <!-- Cover panel -->
  <div class="brand brand--cover">
    <span class="brand__dot"></span>
    <span class="brand__name">GENTLE PAW THERAPY</span>
  </div>
  <div class="photo photo--trio" role="img" aria-label="Juniper, Barnaby and Pepper resting together on a blue couch in front of a brick wall"></div>
  <h1 class="cover-title">Canine<br>Assisted<br>Therapy</h1>
  <div class="leaf-mark leaf-mark--cover" role="img" aria-label="Red maple leaf ornament"></div>
</body>
</html>
```